Update current boring label!!

Help! We need to have our current label redesigned. Initially it was ok but now it needs more punch. We have 3 different products. Vinaigrettes, Balsamic Glazes, and flavored olive oils. I want the same label for all 3 but perhaps in different colors to set the 3 apart. I like clean lines and need something that will be easier to read. Colors I like are black, white, golds, greens and browns.

I like some of the olive oil labels that are out there as they are very clear and easy to read. Same holds true with some Champagne labels.

You all have been so terrific in the past I hope someone can generate a new and wonderful look.

I have attached the current label to use for size.

I look forward to seeing all your wonderful designs.
Updates

Designers,I went on framevault and asked to see all the olive oil labels and there were many labels that I liked a lot. The vintage look is amazing, so please check them out to get an overall feel for what we are looking for.Many thanks,Lorna Added Wednesday, August 9, 2017

Reason: I feel like the label still needs some work. Am looking for that design that without tasting our product SELLS IT!

Target Market(s)

Upscale food buyers. Our products are on the upper end of the spectrum and cost a bit more than others due to their high quality ingredients

Font styles to use
Serif
Decorative
Script

Colors

Designer to choose colors to be used in the design.

Requirements
Must have
• A label that stands out. I see all the wonderful labels that are out there and want something that looks like it's worth more money.
• I would like Marlow to be have more of a punch as well.
Nice to have
• I like the look of white labels with wonderful designs that are easy to read and really stand out. Right now our product is basically plain. The look of champagne labels and olive oil labels. You can get a feel for what I am looking for by looking on line at the different types of labels on bottles.
Should not have
• No pictures just print

```html
<!DOCTYPE html>
<html lang="en">
<head>
<meta charset="utf-8">
<title>Marlow Dressing Labels</title>
<link rel="stylesheet" href="https://fonts.googleapis.com/css2?family=Playfair+Display:wght@400;700&family=Great+Vibes&family=Oswald:wght@300;400&family=Teko:wght@500&display=swap">
<style>
  :root {
    --page: #2a2a2a;
    --label-white: #f7f7f7;
    --label-silver: #dedede;
    --ink: #151515;
    --tag-ink: #3a3a3a;
    --band-black: #1b1811;
    --band-olive: #332f12;
    --band-purple: #4f1b45;
    --accent-olive: #aab12a;
    --accent-cream: #d4d08a;
    --accent-pink: #e58ae0;
    --band-word: #f2f2f2;
  }
  * { margin: 0; padding: 0; box-sizing: border-box; }
  html, body { width: 1200px; height: 890px; overflow: hidden; background: var(--page); }
  .label-row {
    width: 1200px; height: 890px;
    display: flex; justify-content: center; align-items: center; gap: 80px;
  }
  .label {
    position: relative; width: 272px; height: 780px; overflow: hidden;
    background: linear-gradient(90deg, var(--label-silver) 0%, var(--label-white) 30%, var(--label-white) 70%, var(--label-silver) 100%);
  }
  .pour {
    position: absolute; left: 20px; top: 0; width: 22px; height: 600px;
    border-radius: 0 0 11px 11px;
  }
  .label--vinaigrette .pour, .label--oil .pour {
    background: linear-gradient(180deg, rgba(185,191,42,0.9), rgba(185,191,42,0.35));
  }
  .label--glaze .pour {
    background: linear-gradient(180deg, rgba(176,59,166,0.95), rgba(176,59,166,0.35));
  }
  .brand-block {
    position: absolute; left: 52px; right: 10px; top: 120px;
    text-align: center;
  }
  .brand-name {
    display: block;
    font-family: "Playfair Display", serif; font-weight: 400;
    font-size: 40px; line-height: 1.1; letter-spacing: 3px; color: var(--ink);
  }
  .brand-rule {
    display: block; width: 60px; height: 1px; margin: 16px auto 14px;
    background: var(--tag-ink);
  }
  .brand-tagline {
    display: block;
    font-family: "Playfair Display", serif; font-size: 12px;
    letter-spacing: 1.5px; line-height: 1.6; color: var(--tag-ink);
  }
  .flavour {
    position: absolute; top: 440px; left: 52px; right: 10px; text-align: center;
    font-family: "Great Vibes", cursive; font-size: 34px; line-height: 1.25; color: #2b2b2b;
  }
  .product-band {
    position: absolute; left: 0; top: 540px; width: 100%; height: 212px;
    display: flex; flex-direction: column; align-items: center; justify-content: center;
  }
  .label--vinaigrette .product-band { background: var(--band-black); }
  .label--oil .product-band { background: var(--band-olive); }
  .label--glaze .product-band { background: var(--band-purple); }
  .product-type {
    font-family: "Oswald", sans-serif; font-weight: 400; font-size: 38px;
    letter-spacing: 1px; line-height: 1.1;
  }
  .label--vinaigrette .product-type { color: var(--accent-olive); }
  .label--oil .product-type { color: var(--accent-cream); }
  .label--glaze .product-type { color: var(--accent-pink); }
  .product-name {
    font-family: "Teko", sans-serif; font-weight: 500; color: var(--band-word);
    letter-spacing: 2px; line-height: 0.95;
  }
  .label--vinaigrette .product-name { font-size: 46px; }
  .label--oil .product-name { font-size: 70px; }
  .label--glaze .product-name { font-size: 84px; }
</style>
</head>
<body>
  <main class="label-row">
    <section class="label label--vinaigrette">
      <div class="pour" role="img" aria-label="Stream of golden vinaigrette pouring down the label"></div>
      <div class="brand-block">
        <span class="brand-name">MARLOW</span>
        <span class="brand-rule"></span>
        <span class="brand-tagline">SMALL BATCH<br>KITCHEN DRESSINGS</span>
      </div>
      <p class="flavour">Champagne<br>Pear</p>
      <div class="product-band">
        <span class="product-type">PREMIUM</span>
        <span class="product-name">VINAIGRETTE</span>
      </div>
    </section>
    <section class="label label--oil">
      <div class="pour" role="img" aria-label="Stream of green olive oil pouring down the label"></div>
      <div class="brand-block">
        <span class="brand-name">MARLOW</span>
        <span class="brand-rule"></span>
        <span class="brand-tagline">SMALL BATCH<br>KITCHEN DRESSINGS</span>
      </div>
      <p class="flavour">Champagne<br>Pear</p>
      <div class="product-band">
        <span class="product-type">INFUSED</span>
        <span class="product-name">OLIVE OIL</span>
      </div>
    </section>
    <section class="label label--glaze">
      <div class="pour" role="img" aria-label="Stream of purple balsamic glaze pouring down the label"></div>
      <div class="brand-block">
        <span class="brand-name">MARLOW</span>
        <span class="brand-rule"></span>
        <span class="brand-tagline">SMALL BATCH<br>KITCHEN DRESSINGS</span>
      </div>
      <p class="flavour">Champagne<br>Pear</p>
      <div class="product-band">
        <span class="product-type">BALSAMIC</span>
        <span class="product-name">GLAZE</span>
      </div>
    </section>
  </main>
</body>
</html>
```